business card for a massage therapy practice named 'Meadow and Willow Massage Studio'

I really need a trendy, yet easy on the eyes business card to complement my logo. Ideally with some gold or rose gold foil work.

My uploaded file of the logo I have in horizontal but I have a vertical version as well. Another color that is used in the website is a blush pink here and there. I'd like to see some trendy tropical leaves in the design.

```html
<!DOCTYPE html>
<html lang="en">
<head>
<meta charset="utf-8">
<title>Meadow and Willow Massage Studio – Business Card</title>
<link rel="stylesheet" href="https://fonts.googleapis.com/css2?family=Kaushan+Script&family=Amatic+SC:wght@700&display=swap">
<style>
  :root {
    --mint: #8fd2b9;
    --leaf-mid: #4fae8a;
    --leaf: #17895f;
    --panel: #f7fbfa;
    --frame: #8fd2b9;
    --ink: #141414;
    --gold: #a88a5a;
  }
  * { margin: 0; padding: 0; box-sizing: border-box; }
  html, body {
    width: 1200px;
    height: 720px;
    overflow: hidden;
    background: var(--mint);
  }
  .card {
    position: relative;
    width: 1200px;
    height: 720px;
    overflow: hidden;
  }
  .leaf-pattern {
    position: absolute;
    inset: 0;
    background: linear-gradient(150deg, var(--leaf-mid) 0%, var(--leaf) 50%, var(--leaf-mid) 100%);
  }
  .logo-panel {
    position: absolute;
    left: 261px;
    top: 217px;
    width: 678px;
    height: 291px;
    background: var(--panel);
  }
  .logo-frame {
    position: absolute;
    inset: 17px;
    border: 2.5px solid var(--frame);
  }
  .mark {
    position: absolute;
    left: 41px;
    top: 96px;
    width: 100px;
    height: 100px;
    border-radius: 50%;
    background: var(--gold);
  }
  .brand-name {
    position: absolute;
    left: 136px;
    top: 52px;
    width: 500px;
    text-align: center;
    font-family: "Kaushan Script", cursive;
    font-weight: 400;
    font-size: 69px;
    line-height: 1;
    color: var(--ink);
    white-space: nowrap;
  }
  .tagline {
    position: absolute;
    left: 118px;
    top: 194px;
    width: 500px;
    text-align: center;
    font-family: "Amatic SC", sans-serif;
    font-weight: 700;
    font-size: 50px;
    letter-spacing: 9.5px;
    line-height: 1;
    color: var(--frame);
    white-space: nowrap;
  }
</style>
</head>
<body>
  <main class="card">
    <div class="leaf-pattern" role="img" aria-label="Pattern of overlapping tropical palm and monstera leaves in deep green over mint"></div>
    <section class="logo-panel">
      <div class="logo-frame"></div>
      <div class="mark" aria-hidden="true"></div>
      <h1 class="brand-name">Meadow &amp; Willow</h1>
      <p class="tagline">Massage Studio</p>
    </section>
  </main>
</body>
</html>
```